Glimmerseal pond linings website template

We need a template for our new website. Glimmerseal is currently marketed through www.tarpavale.com.au, and we are moving the pond/dam linings to a dedicated site www.glimmerseal.com.au

The site is essentially brochureware. The content (less landing page & photo gallery) is on the new site to give you a better idea of what we do. We are also on Facebook.com/glimmerseal

We are looking for a template/style which we can adapt to the different sections of the site as required. We also get a lot of phone/tablet visitors so an alternative mobile layout would be a bonus, but by no means required.

I am proficient in HTML/CSS & javascript so can code most designs thrown at me.

Any icons or interface fonts should be freely available web fonts where possible.

Target Market(s)

We are targeting both landscape professionals (design & construction) as well as the DIY market for ponds/wateragrdens.

Industry/Entity Type

Moving

Requirements
Must have
• We need a design (preferably layered PSD or AI) as basis for our overall site look and feel. Fonts/iconography/layout are where we are lacking. We can do the HTML/CSS/JS/PHP internally.
Nice to have
• A style guide either in file or separate would be nice.
Layers with effect (i.e.. :hover, CSS3 transition endpoints, etc)

```html
<!DOCTYPE html>
<html lang="en">
<head>
<meta charset="utf-8">
<title>Glimmerseal – Pond Linings</title>
<link rel="stylesheet" href="https://fonts.googleapis.com/css2?family=Fenix&family=PT+Serif:ital,wght@0,400;0,700;1,400;1,700&family=Open+Sans:ital,wght@0,400;0,600;1,400&display=swap">
<style>
  :root {
    --bg-top: #6f9d2d;
    --bg-bottom: #c9db3a;
    --page: #ffffff;
    --navy: #083677;
    --navy-line: #2a5290;
    --green-dark: #11704a;
    --green-btn-top: #4c9a2e;
    --green-btn-bottom: #2f7a1f;
    --olive: #5f8f1a;
    --text: #3c3c3c;
    --heading: #333333;
    --box-bg: #f8f8f8;
    --box-line: #dcdcdc;
    --photo-a: #3f6a33;
    --photo-b: #8a7f5e;
  }
  * { margin: 0; padding: 0; box-sizing: border-box; }
  html, body { width: 1200px; height: 1178px; overflow: hidden; }
  body {
    position: relative;
    background: linear-gradient(180deg, var(--bg-top) 0%, #9cbf35 55%, var(--bg-bottom) 100%);
    font-family: "PT Serif", serif;
    color: var(--text);
  }
  .page {
    position: absolute; left: 120px; top: 35px; width: 960px; height: 1062px;
    background: var(--page); border-radius: 4px;
  }
  .brand {
    position: absolute; left: 13px; top: 58px;
    display: flex; align-items: center; gap: 12px;
    font-family: "Open Sans", sans-serif; font-size: 30px; font-weight: 400;
    letter-spacing: 2px; color: var(--green-dark);
  }
  .brand-mark { width: 34px; height: 34px; background: var(--green-dark); }
  .search {
    position: absolute; left: 726px; top: 47px; width: 217px; height: 32px;
    border: 1px solid #d6d6d6; border-radius: 3px; background: linear-gradient(#fff,#f3f3f3);
    display: flex;
  }
  .search-field {
    flex: 1; padding: 7px 11px; font-family: "Open Sans", sans-serif; font-style: italic;
    font-size: 12px; color: #9a9a9a; border-right: 1px solid #d6d6d6;
  }
  .search-btn { width: 39px; display: flex; align-items: center; justify-content: center; }
  .main-nav {
    position: absolute; left: 10px; top: 120px; width: 940px; height: 44px;
    background: var(--navy); border-radius: 4px; display: flex; padding-left: 4px;
  }
  .main-nav a {
    font-family: "Open Sans", sans-serif; font-size: 12.5px; color: #fff; text-decoration: none;
    display: flex; align-items: center; padding: 0 22px; border-right: 1px solid var(--navy-line);
  }
  .main-nav a:last-child { border-right: none; }
  .main-nav a:hover { background: #0d4592; }
  .hero {
    position: absolute; left: 11px; top: 177px; width: 938px; height: 348px;
    border: 1px solid #cfcfcf; border-radius: 4px;
    background: linear-gradient(160deg, #5f8a3e 0%, #3d5b2e 35%, #7a8a7a 55%, #4f7a35 75%, #5d6a4a 100%);
  }
  .hero-arrow {
    position: absolute; top: 156px; width: 35px; height: 35px; background: rgba(20,20,20,.75);
    display: flex; align-items: center; justify-content: center;
  }
  .hero-arrow.prev { left: 0; } .hero-arrow.next { right: 0; }
  .box { position: absolute; background: var(--box-bg); border: 1px solid var(--box-line); border-radius: 3px; }
  .box-title { font-family: "Fenix", serif; font-weight: 400; }
  .services { left: 10px; top: 570px; width: 220px; height: 280px; padding: 10px 15px; }
  .services .box-title { font-size: 22px; color: var(--heading); margin-bottom: 10px; }
  .services ul { list-style: none; }
  .services li { font-size: 13px; height: 24.8px; display: flex; align-items: center; gap: 11px; }
  .view-more {
    position: absolute; right: 17px; bottom: 10px; font-family: "Open Sans", sans-serif;
    font-style: italic; font-size: 12px; color: var(--olive);
  }
  .testimonials { left: 10px; top: 874px; width: 220px; height: 148px; padding: 10px 15px; }
  .testimonials .box-title { font-size: 22px; color: var(--green-dark); margin-bottom: 8px; }
  .quote { font-size: 11.5px; line-height: 19px; padding-left: 9px; position: relative; }
  .quote::before { content: "\201C"; position: absolute; left: -8px; top: -4px; font: 700 20px "PT Serif", serif; color: var(--navy); }
  .quote-end { font: 700 15px "PT Serif", serif; color: var(--navy); }
  .quote-by { text-align: right; font-style: italic; font-weight: 700; font-size: 13px; color: var(--navy); margin-top: 8px; }
  .welcome { left: 250px; top: 570px; width: 700px; height: 212px; padding: 12px 25px; }
  .welcome .box-title { font-size: 26px; color: var(--green-dark); margin-bottom: 16px; }
  .welcome p { font-size: 12.5px; line-height: 18.5px; margin-bottom: 19px; }
  .btn {
    position: absolute; right: 18px; top: 167px; width: 103px; height: 28px;
    background: linear-gradient(var(--green-btn-top), var(--green-btn-bottom));
    color: #fff; font-weight: 700; font-size: 12.5px; display: flex; align-items: center; justify-content: center;
    border-radius: 2px;
  }
  .gallery { position: absolute; left: 251px; top: 802px; width: 699px; }
  .gallery .box-title { font-size: 22px; color: var(--heading); }
  .gallery-nav { position: absolute; right: 0; top: 8px; display: flex; gap: 4px; }
  .dot { width: 18px; height: 18px; border-radius: 50%; background: radial-gradient(circle at 40% 35%, #a8cc3a, #5f8f12); display: flex; align-items: center; justify-content: center; }
  .gallery p { font-size: 12.5px; line-height: 18.5px; margin-top: 14px; }
  .thumbs { position: absolute; top: 100px; left: -2px; display: flex; gap: 19px; }
  .thumb { width: 221px; height: 131px; border: 1px solid #ddd; padding: 3px; background: #fff; box-shadow: 0 1px 3px rgba(0,0,0,.15); }
  .thumb div { width: 100%; height: 100%; }
  .t1 { background: linear-gradient(135deg, #3a6a2c, #7f8a80 50%, #3f6a2a); }
  .t2 { background: linear-gradient(150deg, #6c8a3a, #4f5f3a 50%, #8a8670); }
  .t3 { background: linear-gradient(160deg, #4a7a35, #8f8c80 50%, #5f8f3a); }
  .footer-note { position: absolute; left: 125px; top: 1125px; font-family: "Open Sans", sans-serif; font-size: 13px; color: #2e3a14; }
  .social { position: absolute; left: 950px; top: 1124px; display: flex; gap: 12px; }
  .social span { width: 30px; height: 30px; border-radius: 50%; }
  .social .s1 { background: #1f3f8f; } .social .s2 { background: #2f9ad8; } .social .s3 { background: #e2571c; }
</style>
</head>
<body>
  <div class="page">
    <div class="brand"><span class="brand-mark"></span>GLIMMERSEAL</div>
    <div class="search">
      <div class="search-field">Search here...</div>
      <div class="search-btn">
        <svg width="24" height="22" viewBox="0 0 24 22"><circle cx="9" cy="9" r="6" fill="none" stroke="#11704a" stroke-width="3"/><line x1="13" y1="13" x2="21" y2="19" stroke="#11704a" stroke-width="4" stroke-linecap="round"/></svg>
      </div>
    </div>
    <nav class="main-nav">
      <a href="#">HOME</a><a href="#">ABOUT US</a><a href="#">HAPPENINGS</a><a href="#">GALLERY</a>
      <a href="#">LINER STYLES</a><a href="#">PREPARATION</a><a href="#">INSTALLATION</a><a href="#">CONTACT US</a>
    </nav>
    <div class="hero" role="img" aria-label="Lined garden pond with ferns, waterfall and a timber ladder">
      <div class="hero-arrow prev"><svg width="8" height="12"><path d="M6 1 1 6l5 5" fill="none" stroke="#fff" stroke-width="1.5"/></svg></div>
      <div class="hero-arrow next"><svg width="8" height="12"><path d="M2 1l5 5-5 5" fill="none" stroke="#fff" stroke-width="1.5"/></svg></div>
    </div>

    <aside class="box services">
      <h2 class="box-title">Our Services</h2>
      <ul>
        <li><svg width="13" height="10"><path d="M0 5h11M7 1l4 4-4 4" fill="none" stroke="#11704a" stroke-width="1.6"/></svg>Lorem ipsum dolor sit amet,</li>
        <li><svg width="13" height="10"><path d="M0 5h11M7 1l4 4-4 4" fill="none" stroke="#11704a" stroke-width="1.6"/></svg>Consectetur adipisicing</li>
        <li><svg width="13" height="10"><path d="M0 5h11M7 1l4 4-4 4" fill="none" stroke="#11704a" stroke-width="1.6"/></svg>Sed do eiusmod</li>
        <li><svg width="13" height="10"><path d="M0 5h11M7 1l4 4-4 4" fill="none" stroke="#11704a" stroke-width="1.6"/></svg>Incididunt ut labore et</li>
        <li><svg width="13" height="10"><path d="M0 5h11M7 1l4 4-4 4" fill="none" stroke="#11704a" stroke-width="1.6"/></svg>Dolore magna aliqua.</li>
        <li><svg width="13" height="10"><path d="M0 5h11M7 1l4 4-4 4" fill="none" stroke="#11704a" stroke-width="1.6"/></svg>Ut enim ad minim veniam.</li>
        <li><svg width="13" height="10"><path d="M0 5h11M7 1l4 4-4 4" fill="none" stroke="#11704a" stroke-width="1.6"/></svg>Sed do eiusmod</li>
        <li><svg width="13" height="10"><path d="M0 5h11M7 1l4 4-4 4" fill="none" stroke="#11704a" stroke-width="1.6"/></svg>Incididunt ut labore et</li>
      </ul>
      <span class="view-more">View More &gt;&gt;</span>
    </aside>

    <aside class="box testimonials">
      <h2 class="box-title">Testimonials</h2>
      <p class="quote">Ut enim ad minim veniam, quisnos trud exercitation ullamco laboris nisi ut aliquip ex ea commodo.<span class="quote-end">&#8221;</span></p>
      <p class="quote-by">by Mara Delvin</p>
    </aside>

    <section class="box welcome">
      <h1 class="box-title">Welcome to Our Website..</h1>
      <p>Lorem ipsum dolor sit amet, consectetur adipisicing elit, sed do eiusmod tempor incididunt ut labore et dolore magna aliqua. Ut enim ad minim veniam, quis nostrud exercitation ullamco laboris nisi ut aliquip ex ea commodo consequat. Duis aute irure dolor in reprehenderit involuptate velit esse cillum.</p>
      <p>Ut enim ad minim veniam, quis nostrud exercitation ullamco laboris nisi ut aliquip ex ea commodo consequat.</p>
      <span class="btn">Read More</span>
    </section>

    <section class="gallery">
      <h2 class="box-title">Our Gallery</h2>
      <div class="gallery-nav">
        <span class="dot"><svg width="6" height="8"><path d="M5 0 0 4l5 4z" fill="#fff"/></svg></span>
        <span class="dot"><svg width="6" height="8"><path d="M1 0l5 4-5 4z" fill="#fff"/></svg></span>
      </div>
      <p>Lorem ipsum dolor sit amet, consectetur adipisicing elit, sed do eiusmod tempor incididunt ut labore et dolore magna aliqua. Ut enim ad minim veniam, quis nostrud exercitation ullamco laboris nis.</p>
      <div class="thumbs">
        <div class="thumb"><div class="t1" role="img" aria-label="Pond waterfall among tree ferns"></div></div>
        <div class="thumb"><div class="t2" role="img" aria-label="Clear shallow pond with a fallen log"></div></div>
        <div class="thumb"><div class="t3" role="img" aria-label="Pond edged with boulders and reeds"></div></div>
      </div>
    </section>
  </div>

  <p class="footer-note">&copy;2013. Glimmerseal. All Right Reserved.</p>
  <div class="social" aria-label="Social links"><span class="s1"></span><span class="s2"></span><span class="s3"></span></div>
</body>
</html>
```